屋号は
柏谷バル
赤帽子のMILO
です。看板の大きさは横4メートル縦3メートル位です。目立ち、入りやすい看板がいいです。
黒ひげのキャラクターゆるカッコイイ感じ。シャツにもロゴ入れ予定。
樽とピザとチーズでの〇△□のロゴ
メニュー名、【ミロハイボール、ワイン、骨付きチキン、ピザ】入り
柏谷バル赤帽子のMILO

ミロハイボール、ワイン、骨付きチキン、ピザ

赤系、緑系、グレー系、背景は白がいいです。
1店舗目のロゴをイタリアンに崩したロゴを兄弟店だと分かるように入れたいと考えています。
参考モデルはザクザクチキンと言うチェーンのバルです。
1店舗目のロゴ画像貼り付け致します。
提案が思っていた以上に少なかった為、延長させて頂きます。是非皆様宜しくおねがいしますm(__)m

沢山案を出して頂き、1番思い描いた形に近かったからです。対応も早く助かりました。

今回はとてもザックリな件に提案して頂きありがとうございました。とても素晴らしい案が沢山あり、とても悩みました。本当にありがとうございました。また機会がありましたら宜しくおねがいしますm(__)m

```html
<!DOCTYPE html>
<html lang="ja">
<head>
<meta charset="utf-8">
<title>柏谷バル赤帽子のMILO 看板</title>
<link rel="stylesheet" href="https://fonts.googleapis.com/css2?family=Noto+Sans+JP:wght@700;900&family=Roboto:wght@900&family=Kaushan+Script&display=swap">
<style>
  :root {
    --ink: #0b0b0b;
    --paper: #ffffff;
    --yellow: #fff200;
    --red: #e8141c;
    --mascot-grey: #58585a;
    --skewer-tone: #c98a3a;
  }
  * { margin: 0; padding: 0; box-sizing: border-box; }
  html, body { width: 1200px; height: 900px; overflow: hidden; background: var(--paper); }
  .signboard {
    position: relative;
    width: 1200px;
    height: 900px;
    background: var(--paper);
    font-family: "Noto Sans JP", sans-serif;
    color: var(--ink);
  }
  .menu-band {
    position: absolute;
    left: 0;
    width: 1200px;
    background: var(--ink);
    color: var(--yellow);
    font-weight: 900;
    display: flex;
    align-items: center;
    line-height: 1;
  }
  .menu-band--top {
    top: 0;
    height: 138px;
    justify-content: center;
    font-size: 84px;
    letter-spacing: 2px;
  }
  .menu-band--bottom {
    bottom: 0;
    height: 138px;
    padding-left: 48px;
    font-size: 78px;
  }
  .welcome-tab {
    position: absolute;
    right: 0;
    bottom: 0;
    width: 344px;
    height: 138px;
    background: var(--red);
    clip-path: polygon(32px 0, 100% 0, 100% 100%, 0 100%);
    display: flex;
    align-items: center;
    justify-content: center;
    padding-left: 30px;
    color: var(--paper);
    font-family: "Kaushan Script", cursive;
    font-size: 62px;
  }
  .mascot {
    position: absolute;
    left: 90px;
    top: 192px;
    width: 294px;
    height: 534px;
    border-radius: 140px 140px 60px 60px;
    background: linear-gradient(180deg, var(--ink) 0%, var(--ink) 30%, var(--mascot-grey) 55%, var(--mascot-grey) 100%);
  }
  .shop-name {
    position: absolute;
    left: 432px;
    top: 262px;
    font-size: 166px;
    font-weight: 900;
    line-height: 1;
    letter-spacing: 6px;
  }
  .shop-subname {
    position: absolute;
    left: 436px;
    top: 448px;
    font-size: 86px;
    font-weight: 900;
    line-height: 1.1;
    letter-spacing: 1px;
  }
  .shop-subname .accent { color: var(--red); font-family: "Roboto", "Noto Sans JP", sans-serif; }
  .romaji {
    position: absolute;
    left: 444px;
    top: 572px;
    font-family: "Roboto", sans-serif;
    font-weight: 900;
    line-height: 1;
  }
  .romaji-main { font-size: 46px; display: block; }
  .romaji-sub { font-size: 30px; display: block; margin-top: 10px; }
  .food-skewer {
    position: absolute;
    left: 860px;
    top: 564px;
    width: 240px;
    height: 96px;
    border-radius: 48px;
    background: linear-gradient(90deg, #8b5a2b 0%, var(--skewer-tone) 40%, #e05a2a 65%, #f6c21c 100%);
  }
</style>
</head>
<body>
<main class="signboard">
  <header class="menu-band menu-band--top">赤帽子ハイボール、ワイン</header>

  <div class="mascot" role="img" aria-label="大きな帽子と口ひげのキャラクターがジョッキを持って立つイラスト"></div>

  <h1 class="shop-name">柏谷バル</h1>
  <p class="shop-subname">赤帽子の<span class="accent">MILO</span></p>
  <p class="romaji">
    <span class="romaji-main">KASHIWAYA BAL</span>
    <span class="romaji-sub">AKABOUSHI NO MILO</span>
  </p>
  <div class="food-skewer" role="img" aria-label="骨付き肉・樽・ピザ・チーズを串に刺したイラスト"></div>

  <footer class="menu-band menu-band--bottom">骨付きチキン、ピザ</footer>
  <div class="welcome-tab">Welcome</div>
</main>
</body>
</html>
```